New logo and packaging for Chicago based skincare company

Tesquin needs a new logo and packaging to help in marketing our new anti-aging skincare line.

About Us
We're quirky, skin-obsessed beauty geeks with a knack for research and a love for all things skincare. Our ambition to create REAL products with exotic ingredients inspired the name Tesquin which translates to peau + jolie meaning beautiful skin in french.

Our Products
We strive to do it differently. We develop high potency, natural skincare products using top of the line, novel ingredients imported from all over the globe. Our products are made in the USA and free from gluten, parabens, sulfates, and useless fillers that can't deliver.
Price range: $25-75 (moderate)

LOGO
Open to any color/typography except red and purple. Should also be: modern, feminine, cultured, neutral, vibrant, simple, timeless, and sophisticated

LABEL
Logo placed on label, but should not be the focal point of product. EGF SERUM should grab attention of quick glancers
The ideal label design pairs neutrals with brights while achieving balance between minimalism and complexity.
Incorporates some sort of unconventionality, boldness, or uniqueness without adding distraction.

Color: Mostly white or silver background with splash of color (no purple, light pinks, or red). See attached kraft color chart for direction. Bright blues (teal, cobalt, navy, sky blue, and greens are ideal)

Target Market(s)

Target audience: Socially and health conscious women, cultured, ages 25-60, seeks high quality natural products with effective ingredients.

Industry/Entity Type

Skin Care Product

Logo Text

Tesquin

Font styles to use
Other font styles liked:
• Open

Colors
f6f6f6
ffffff
fdfdfd
eeeeee
fbfbfb
0255a3
3176b5
33a6d7
86cfc6

Requirements
Must have
• Packaging includes:
• 1 oz amber glass bottles with white dropper - see attached image
• Dimensions: 1.25" width by 4.1" height
• Label should wrap around bottle similar to peptide complex image and includes ingredient list; Logo should be not focal point of label
• Green (peptide complex) label shows ideal clarity
• "Zenthra" can be written in several different ways, feel free to get creative
• Label Text:
• EGF
• ZENTHRA
• SERUM
• Anti-aging Skin firming Scar removal
• 1 FL OZ (30ml)
• Ingredients:
• Hamamelis Virginiana (Witch Hazel) Water, Aqua (Water), Alcohol, Glycerin, Polysorbate 20, rh-Oligopeptide-1(EGF), Caprooyl Tetrapeptide-3, Cocos Nucifera (Coconut) Fruit Juice, Lavandula Angustifolia (Lavender) Oil, Citrus
• Paradisi (Pink Grapefruit) Peel Oil*, Citrus Aurantium Dulcis (Orange) Peel Oil*, Santalum Austrocaledonicum (Sandalwood) Wood Oil, Boswellia Carterii (Frankincense) Oil, Rosa Damascena Flower Oil, Dextran, Xanthan Gum,
• Gluconolactone, Sodium Benzoate
• Directions:
• Apply a small amount of EGF serum to clean skin once or twice daily. Allow to dry. Can be used both morning and night, and under makeup. Follow with moisturizer.
• Caution: For external use only. Use only as directed. Avoid contact with eyes. If contact occurs, rinse well with water.
• Distributed by Tesquin, LLC
• Munster, Indiana 46321
• Made in USA, FDA Registered lab (please use symbols for these)
Nice to have
• Either or: White space, silver, boldness, numbers, kraft colors (see attached) shapes, geometric patterns, minimalism
• Label: Incorporate shapes and dimensions with minimal/bare background
• Open to handwritten fonts if clear and easy to read
Should not have
• No more than 3-4 colors, look too busy, cursive fonts

```html
<!DOCTYPE html>
<html lang="en">
<head>
<meta charset="utf-8">
<title>Tesquin EGF Zenthra Serum – Label</title>
<link href="https://fonts.googleapis.com/css2?family=PT+Sans:ital,wght@0,400;0,700;1,400;1,700&display=swap" rel="stylesheet">
<style>
  :root {
    --page-bg: #f3f3f3;
    --label-white: #ffffff;
    --band-grey: #a9abae;
    --accent-orange: #ee7a2e;
    --accent-orange-deep: #e2651c;
    --ink-white: #ffffff;
    --ink-dark: #2a2a2a;
  }
  * { margin: 0; padding: 0; box-sizing: border-box; }
  html, body {
    width: 1200px;
    height: 1000px;
    overflow: hidden;
    background: var(--page-bg);
    font-family: "PT Sans", "Helvetica Neue", Arial, sans-serif;
  }
  .label {
    position: absolute;
    left: 320px;
    top: 70px;
    width: 560px;
    height: 860px;
    background: var(--label-white);
    box-shadow: 0 2px 14px rgba(0,0,0,0.08);
  }
  .label-shapes {
    position: absolute;
    inset: 0;
    width: 560px;
    height: 860px;
  }
  .brand {
    position: absolute;
    top: 110px;
    left: 0;
    width: 100%;
    display: flex;
    justify-content: center;
    align-items: center;
    gap: 22px;
  }
  .brand-name {
    color: var(--accent-orange);
    font-size: 40px;
    font-weight: 400;
    letter-spacing: 0.28em;
    text-transform: uppercase;
  }
  .brand-dot {
    width: 30px;
    height: 30px;
    border-radius: 50%;
    background: var(--accent-orange);
  }
  .product-title {
    position: absolute;
    top: 318px;
    left: 0;
    width: 100%;
    text-align: center;
    color: var(--ink-white);
    font-weight: 700;
    font-size: 112px;
    line-height: 0.98;
    letter-spacing: -0.01em;
  }
  .product-title span { display: block; }
  .tagline {
    position: absolute;
    top: 668px;
    left: 60px;
    width: 440px;
    text-align: center;
    color: var(--ink-white);
    font-style: italic;
    font-weight: 700;
    font-size: 25px;
    line-height: 1.25;
  }
  .net-contents {
    position: absolute;
    top: 808px;
    left: 0;
    width: 100%;
    text-align: center;
    color: var(--ink-dark);
    font-weight: 700;
    font-size: 17px;
    letter-spacing: 0.01em;
  }
</style>
</head>
<body>
  <div class="label">
    <svg class="label-shapes" viewBox="0 0 560 860" aria-hidden="true">
      <defs>
        <linearGradient id="panelFill" x1="0" y1="0" x2="0" y2="1">
          <stop offset="0" stop-color="#f08236"/>
          <stop offset="1" stop-color="#e2651c"/>
        </linearGradient>
      </defs>
      <polygon class="band-top" points="0,272 560,206 560,226 0,292" fill="var(--band-grey)"/>
      <polygon class="accent-panel" points="0,296 560,230 560,742 0,788" fill="url(#panelFill)"/>
      <polygon class="band-bottom" points="160,776 560,742 560,752 160,786" fill="var(--band-grey)"/>
    </svg>

    <div class="brand">
      <span class="brand-name">Tesquin</span>
      <span class="brand-dot"></span>
    </div>

    <h1 class="product-title">
      <span>EGF</span>
      <span>ZENTHRA</span>
      <span>SERUM</span>
    </h1>

    <p class="tagline">Anti-aging Skin firming Cell renewal Scar removal</p>

    <p class="net-contents">NET CONTENTS 1 FL. OZ. (30 ml)</p>
  </div>
</body>
</html>
```